Non fiction leadership Book Cover design needed for “Keep Bold: Begin Owning Daily”

I need a front cover design for a new book 6 X 9 traditional non-fiction book.

Title: "Keep BOLD - Begin Owning Daily"

The subtitle is not finalized- so use 2 lines of smaller dummy text

My brand guide is attached (please use the tan color sparingly)

I'd like to see BOLD look like it is in motion and "flying" across the page

Need CREATIVE designs and options

Do not want my picture on the front cover - I do want it on the back cover.

On the front cover I’d like to see creative use of font to create movement on “BOLD”

Target Market(s)

Business leaders

Industry/Entity Type

Aviation

Font styles to use
Other font styles liked:
• See style guide- can add additional font (modern script or san serif)

Colors
0054AA
0677BA
7BADD7
CADEEF
E8F1F8
EB3D1F
EC4F4E
F09395
F8D3D4
FCEDEE

Requirements
Must have
• Creative font use, using perspective to create movement/motion on BOLD
Should not have
• My picture on the front cover- my picture should be on the back cover

```html
<!DOCTYPE html>
<html lang="en">
<head>
<meta charset="UTF-8">
<title>Keep Bold: Begin Owning Daily — Book Cover</title>
<link rel="stylesheet" href="https://fonts.googleapis.com/css2?family=Kaushan+Script&family=Bebas+Neue&display=swap">
<style>
  :root {
    --cover-blue: #0054AA;
    --sky-blue: #0677BA;
    --mist-blue: #7BADD7;
    --pale-blue: #CADEEF;
    --signal-red: #EB3D1F;
    --coral-red: #EC4F4E;
    --ink-white: #FFFFFF;
  }
  html, body {
    margin: 0;
    padding: 0;
    width: 800px;
    height: 1200px;
    overflow: hidden;
    background: var(--cover-blue);
  }
  .cover {
    position: relative;
    width: 800px;
    height: 1200px;
    background: var(--cover-blue);
    color: var(--ink-white);
    overflow: hidden;
  }
  .title {
    margin: 0;
    font-weight: 400;
  }
  .title-line {
    position: absolute;
    left: 0;
    width: 800px;
    text-align: center;
    font-family: "Kaushan Script", cursive;
    line-height: 1;
    white-space: nowrap;
  }
  .title-keep {
    top: 40px;
    font-size: 250px;
    letter-spacing: -6px;
  }
  .title-bold-wrap {
    position: absolute;
    top: 318px;
    left: 0;
    width: 800px;
    height: 160px;
    perspective: 420px;
  }
  .speed-lines {
    position: absolute;
    top: 0;
    left: 0;
    width: 800px;
    height: 160px;
  }
  .speed-lines line {
    stroke-linecap: round;
  }
  .title-bold {
    position: absolute;
    top: 8px;
    left: 0;
    width: 800px;
    text-align: center;
    font-family: "Kaushan Script", cursive;
    font-size: 138px;
    line-height: 1;
    letter-spacing: 2px;
    white-space: nowrap;
    color: var(--ink-white);
    transform: rotateY(-28deg) skewX(-14deg);
    transform-origin: 30% 50%;
    text-shadow:
      -14px 0 0 rgba(123, 173, 215, 0.55),
      -28px 0 0 rgba(123, 173, 215, 0.32),
      -42px 0 0 rgba(123, 173, 215, 0.16),
      6px 6px 0 var(--signal-red);
  }
  .title-begin {
    top: 470px;
    font-size: 205px;
    letter-spacing: -4px;
  }
  .title-owning {
    top: 715px;
    font-size: 108px;
    letter-spacing: -3px;
  }
  .subtitle {
    position: absolute;
    top: 932px;
    left: 0;
    width: 800px;
    margin: 0;
    text-align: center;
    font-family: "Bebas Neue", sans-serif;
    font-size: 44px;
    line-height: 57px;
    letter-spacing: 3.5px;
    color: var(--pale-blue);
  }
  .author {
    position: absolute;
    top: 1096px;
    left: 0;
    width: 800px;
    margin: 0;
    text-align: center;
    font-family: "Bebas Neue", sans-serif;
    font-size: 66px;
    line-height: 1;
    letter-spacing: 5px;
  }
</style>
</head>
<body>
  <main class="cover">
    <h1 class="title">
      <span class="title-line title-keep">Keep</span>
      <span class="title-bold-wrap">
        <svg class="speed-lines" viewBox="0 0 800 160" aria-hidden="true">
          <line x1="60" y1="52" x2="210" y2="52" stroke="#7BADD7" stroke-width="6"/>
          <line x1="20" y1="82" x2="200" y2="82" stroke="#EC4F4E" stroke-width="6"/>
          <line x1="80" y1="112" x2="215" y2="112" stroke="#7BADD7" stroke-width="6"/>
        </svg>
        <span class="title-bold">BOLD</span>
      </span>
      <span class="title-line title-begin">Begin</span>
      <span class="title-line title-owning">Owning Daily</span>
    </h1>
    <p class="subtitle">Unlock your inner potential<br>and soar to new heights</p>
    <p class="author">Author Name</p>
  </main>
</body>
</html>
```